Professional and creative business card design for recruiting service providers

Our company supports German medium-sized companies in filling vacancies promptly. For this we use social media marketing and bring our customers into the visibility.

We want a professional but also creative design for our business cards.

Please look at halvenrick-consult.de to get an impression of our CI.

Target Market(s)

Small and medium-sized companies in Germany from the industry

Industry/Entity Type

Industrie, Handwerk

Contact Information for Business Card

Name, Position, Telefonnummer, Email, Website

Colors
EE7325
F08F49
F5BC92
FAE3D3
FDF4ED

Requirements
Must have
• A picture of the employee and in the style of www.halvenrick-consult.de

```html
<!DOCTYPE html>
<html lang="de">
<head>
<meta charset="utf-8">
<title>Halvenrick &amp; Partner – Visitenkarte</title>
<link href="https://fonts.googleapis.com/css2?family=Montserrat:wght@600;700;800&family=Arimo:wght@400;700&display=swap" rel="stylesheet">
<style>
  :root {
    --stage: #2b2725;
    --card: #1a1a1a;
    --card-back: #1c1c1c;
    --photo-bg: #333333;
    --orange: #ee5a24;
    --white: #ffffff;
    --rule: #5a5a5a;
  }
  * { box-sizing: border-box; margin: 0; padding: 0; }
  html, body {
    width: 1200px; height: 842px; overflow: hidden;
    background: var(--stage);
  }
  .canvas {
    position: relative; width: 1200px; height: 842px;
    display: flex; align-items: center; justify-content: center; gap: 40px;
  }
  .card {
    position: relative; width: 540px; height: 310px; overflow: hidden;
    box-shadow: 0 14px 30px rgba(0,0,0,.45);
  }

  /* Front */
  .card--front { background: var(--card); }
  .band {
    position: absolute; left: 0; right: 0; height: 12px; background: var(--orange);
  }
  .band--top { top: 10px; }
  .band--bottom { bottom: 10px; }
  .portrait {
    position: absolute; left: 48px; top: 66px; width: 190px; height: 190px;
    background: linear-gradient(160deg, #3a3a3a 0%, #2e2e2e 60%, #1f1f24 100%);
  }
  .divider {
    position: absolute; left: 268px; top: 76px; width: 1px; height: 170px;
    background: var(--rule);
  }
  .details {
    position: absolute; left: 290px; top: 94px; color: var(--white);
    font-family: "Arimo", Arial, sans-serif;
  }
  .details__name {
    font-family: "Montserrat", Arial, sans-serif; font-weight: 700;
    color: var(--orange); font-size: 20px; letter-spacing: .3px; line-height: 1;
  }
  .details__role { font-size: 14px; margin-top: 4px; }
  .contacts { list-style: none; margin-top: 28px; }
  .contacts li {
    display: flex; align-items: center; gap: 8px;
    font-size: 13.5px; line-height: 22px;
  }
  .contacts svg { width: 14px; height: 14px; flex: none; }
  .accent { color: var(--orange); }

  /* Back */
  .card--back { background: var(--card-back); }
  .tab { position: absolute; background: var(--orange); }
  .tab--left { left: 0; top: 168px; width: 28px; height: 62px; }
  .tab--right { right: 0; top: 52px; width: 28px; height: 62px; }
  .brand {
    position: absolute; left: 130px; top: 118px;
    display: flex; align-items: center; gap: 18px;
  }
  .brand__square { width: 62px; height: 62px; background: var(--orange); }
  .brand__name {
    font-family: "Montserrat", Arial, sans-serif; font-weight: 800;
    color: var(--white); font-size: 24px; line-height: 1.1; letter-spacing: 1.5px;
  }
</style>
</head>
<body>
<main class="canvas">
  <section class="card card--front" aria-label="Vorderseite">
    <div class="band band--top"></div>
    <div class="portrait" role="img" aria-label="Porträtfoto des Mitarbeiters vor dunkelgrauem Hintergrund"></div>
    <div class="divider"></div>
    <div class="details">
      <h1 class="details__name">LUKAS BRENNER</h1>
      <p class="details__role">Managing Director</p>
      <ul class="contacts">
        <li>
          <svg viewBox="0 0 24 24" fill="var(--orange)"><path d="M6.6 10.8a15.1 15.1 0 0 0 6.6 6.6l2.2-2.2a1 1 0 0 1 1-.25 11.4 11.4 0 0 0 3.6.57 1 1 0 0 1 1 1V20a1 1 0 0 1-1 1A17 17 0 0 1 3 4a1 1 0 0 1 1-1h3.5a1 1 0 0 1 1 1c0 1.25.2 2.45.57 3.57a1 1 0 0 1-.25 1z"/></svg>
          040-987 654 321
        </li>
        <li>
          <svg viewBox="0 0 24 24" fill="var(--orange)"><path d="M2 5h20v14H2z" fill="none" stroke="var(--orange)" stroke-width="2"/><path d="M2 5l10 8 10-8" fill="none" stroke="var(--orange)" stroke-width="2"/></svg>
          info@halvenrick-consult.de
        </li>
        <li>
          <svg viewBox="0 0 24 24" fill="none" stroke="var(--orange)" stroke-width="2"><circle cx="12" cy="12" r="9"/><path d="M3 12h18M12 3c3 3.2 3 14.8 0 18M12 3c-3 3.2-3 14.8 0 18"/></svg>
          <span>www.<span class="accent">halvenrick-consult</span>.de</span>
        </li>
      </ul>
    </div>
    <div class="band band--bottom"></div>
  </section>

  <section class="card card--back" aria-label="Rückseite">
    <div class="tab tab--left"></div>
    <div class="tab tab--right"></div>
    <div class="brand">
      <div class="brand__square"></div>
      <p class="brand__name">HALVENRICK<br>&amp; PARTNER</p>
    </div>
  </section>
</main>
</body>
</html>
```